Business Card

I need a cool business card for Quill Films. You created logo for me so I'm thinking of using you for my business card. I want something simple, clean, artsy, but yet catchy to eye. I was thinking logo on one side and the information on the other. On teh phone, web, email, fb, and vimeo it would be cool to have the icons to identify each one. I would need these business cards formatted for prenta mart. If you have any recommendations for the card I'm fine with that. I might have to much information not sure.

Logo on one side

Dorn Vallick
Owner/Film Director
phone: 555.207.6183
web: quillfilms.example
email: dorn@quillfilms.example
FB: friendspage.example/quillfilmsLA
Vimeo: clipvault.example/user51093264

The other design I need is:
Marlo Pennick
Film Director/Editing
phone: 555.730.9164
web: quillfilms.example
email: marlo@quillfilms.example

Thanks

```html
<!DOCTYPE html>
<html lang="en">
<head>
<meta charset="utf-8">
<title>Quill Films – Business Card</title>
<link rel="stylesheet" href="https://fonts.googleapis.com/css2?family=Mulish:wght@400;700&display=swap">
<style>
  :root {
    --page: #d9d9d6;
    --card-light: #ffffff;
    --card-shade: #d6d6d6;
    --ink: #1b1b1b;
    --ink-soft: #2a2a2a;
    --brand-red: #e5172f;
    --panel-black: #151515;
    --social-navy: #2d4a86;
    --social-teal: #1aa3c9;
  }
  * { box-sizing: border-box; margin: 0; padding: 0; }
  html, body {
    width: 1200px; height: 871px; overflow: hidden;
    background: var(--page);
    font-family: "Mulish", sans-serif;
    color: var(--ink);
  }
  .stage { position: relative; width: 1200px; height: 871px; }

  .card {
    position: absolute;
    width: 580px; height: 332px;
    overflow: hidden;
    box-shadow: 0 6px 18px rgba(0,0,0,0.25);
  }

  /* Logo side */
  .card-front {
    left: 90px; top: 100px;
    background: linear-gradient(135deg, var(--card-light) 0%, #ececec 45%, var(--card-shade) 100%);
    display: flex; align-items: center; justify-content: center; gap: 18px;
  }
  .brand-dot {
    width: 54px; height: 54px; border-radius: 50%;
    background: var(--brand-red);
  }
  .brand-name {
    font-size: 58px; font-weight: 400; letter-spacing: -1px;
    color: var(--ink);
  }

  /* Info side */
  .card-back {
    left: 530px; top: 440px;
    background: linear-gradient(120deg, #e4e4e4 0%, var(--card-light) 55%, #f2f2f2 100%);
  }
  .back-panel {
    position: absolute; inset: 0;
    width: 100%; height: 100%;
  }
  .panel-brand {
    position: absolute; left: 22px; top: 132px;
    display: flex; align-items: center; gap: 12px;
  }
  .panel-brand .brand-dot { width: 34px; height: 34px; }
  .panel-brand .brand-name { font-size: 30px; color: #ffffff; letter-spacing: 0; }

  .contact {
    position: absolute; right: 34px; top: 92px;
    text-align: right;
  }
  .person-name { font-size: 17px; font-weight: 700; color: var(--ink); }
  .person-role { font-size: 13px; color: var(--ink-soft); margin-top: 3px; }
  .contact-list { list-style: none; margin-top: 30px; }
  .contact-item {
    display: flex; align-items: center; justify-content: flex-end; gap: 14px;
    font-size: 12.5px; line-height: 21px; color: var(--ink-soft);
  }
  .contact-icon { width: 11px; height: 11px; flex: none; }
  .icon-social { width: 10px; height: 10px; border-radius: 2px; }
  .icon-social.is-friends { background: var(--social-navy); }
  .icon-social.is-clips { background: var(--social-teal); }
</style>
</head>
<body>
<main class="stage">

  <section class="card card-front" aria-label="Business card, logo side">
    <span class="brand-dot"></span>
    <span class="brand-name">Quill Films</span>
  </section>

  <section class="card card-back" aria-label="Business card, contact side">
    <svg class="back-panel" viewBox="0 0 580 332" preserveAspectRatio="none" aria-hidden="true">
      <polygon points="0,0 200,0 175,332 0,332" fill="var(--panel-black)"/>
      <polygon points="200,0 270,0 190,332 175,332" fill="var(--brand-red)"/>
    </svg>

    <div class="panel-brand">
      <span class="brand-dot"></span>
      <span class="brand-name">Quill Films</span>
    </div>

    <div class="contact">
      <p class="person-name">Dorn Vallick</p>
      <p class="person-role">Owner/Film Director</p>
      <ul class="contact-list">
        <li class="contact-item">555.207.6183
          <svg class="contact-icon" viewBox="0 0 12 12" aria-label="phone"><path d="M1 3.5C1 2 2.5 1 6 1s5 1 5 2.5V5H8.5V3.8h-5V5H1z M3 6h6l1.5 4.5h-9z" fill="var(--brand-red)"/></svg>
        </li>
        <li class="contact-item">dorn@quillfilms.example
          <svg class="contact-icon" viewBox="0 0 12 12" aria-label="email"><rect x="1" y="2.5" width="10" height="7" fill="none" stroke="var(--brand-red)" stroke-width="1.2"/><path d="M1 2.5l5 4 5-4" fill="none" stroke="var(--brand-red)" stroke-width="1.2"/></svg>
        </li>
        <li class="contact-item">quillfilms.example
          <svg class="contact-icon" viewBox="0 0 12 12" aria-label="web"><circle cx="6" cy="6" r="5" fill="none" stroke="var(--brand-red)" stroke-width="1.2"/><ellipse cx="6" cy="6" rx="2" ry="5" fill="none" stroke="var(--brand-red)" stroke-width="1"/><path d="M1 6h10" stroke="var(--brand-red)" stroke-width="1"/></svg>
        </li>
        <li class="contact-item">friendspage.example/quillfilmsLA
          <span class="contact-icon icon-social is-friends" aria-label="social page"></span>
        </li>
        <li class="contact-item">clipvault.example/user51093264
          <span class="contact-icon icon-social is-clips" aria-label="video page"></span>
        </li>
      </ul>
    </div>
  </section>

</main>
</body>
</html>
```